Change of trading name, rebrand

existing website to be updated with new theme and logo. existing website is
www.brambleworth.com.au
Industry/Entity Type
Construction
Coding
Coded - Design and coding required
Number of Pages Required
5+ page
Requirements
Must have
- be mobile phone friendly

```html
<!DOCTYPE html>
<html lang="en">
<head>
<meta charset="utf-8">
<title>BWH Plant Hire</title>
<link href="https://fonts.googleapis.com/css2?family=Poppins:wght@400;500;600;700;800&display=swap" rel="stylesheet">
<style>
:root{
  --navy:#1f2478;
  --yellow:#f5b400;
  --cream:#fdebc4;
  --white:#ffffff;
  --ink:#2b2b2b;
  --muted:#555a66;
  --line:#e2e2e2;
}
*{box-sizing:border-box;margin:0;padding:0}
html,body{width:1200px;height:3784px;overflow:hidden}
body{position:relative;font-family:"Poppins",sans-serif;color:var(--ink);background:var(--white)}
.abs{position:absolute}
.btn{position:absolute;display:flex;align-items:center;justify-content:center;gap:8px;font-weight:700;font-size:11px;letter-spacing:.5px;text-transform:uppercase;border-radius:4px}
.btn .arrow{font-size:10px}

/* header */
.site-header{left:0;top:0;width:1200px;height:62px;background:var(--white)}
.brand{display:flex;align-items:center;gap:8px;font-weight:800;color:var(--navy)}
.brand .mark{width:14px;height:14px;background:var(--navy)}
.header-brand{left:188px;top:18px;font-size:18px}
.main-nav{left:402px;top:24px;display:flex;gap:29px;font-size:10.5px;color:var(--ink)}
.main-nav .active{color:var(--navy);font-weight:700}
.header-cta{left:893px;top:15px;width:119px;height:33px;background:var(--yellow);color:var(--white)}

/* hero */
.hero{left:0;top:62px;width:1200px;height:552px;background:linear-gradient(180deg,#2c5fa8 0%,#6d97c9 28%,#d9dde2 40%,#a8916c 58%,#7d6a4f 100%)}
.hero-title{left:188px;top:168px;width:824px;font-size:66px;font-weight:800;letter-spacing:16px;color:var(--white);white-space:nowrap}
.hero-title span{color:var(--yellow)}
.hero-dots{left:520px;top:582px;display:flex;gap:14px;align-items:center}
.hero-dots i{width:9px;height:9px;border-radius:50%;background:var(--white);display:block}
.hero-dots i.on{width:14px;height:14px;background:transparent;border:2px solid var(--white)}

/* stats */
.stat{top:670px;width:170px;text-align:center;transform:translateX(-50%)}
.stat svg{display:block;margin:0 auto 8px}
.stat .num{font-size:32px;font-weight:700;color:var(--navy);line-height:1.1}
.stat .label{font-size:9px;font-weight:500;color:var(--ink);text-transform:uppercase;letter-spacing:.3px;line-height:1.5;margin-top:4px}
.divider{top:654px;width:1px;height:144px;background:var(--line)}

/* fleet */
.fleet-band{left:0;top:834px;width:1200px;height:804px;background:var(--cream)}
.fleet-tab{top:911px;width:110px;height:109px;border:1.5px solid #9a9a9a;border-radius:4px;display:flex;flex-direction:column;align-items:center;justify-content:center;gap:12px;font-size:11px;font-weight:500;color:var(--ink)}
.fleet-tab.active{border-color:var(--yellow);color:var(--yellow);background:#fde7b8;box-shadow:0 8px 18px rgba(0,0,0,.12)}
.fleet-card{left:188px;top:1071px;width:824px;height:391px;background:var(--white);border-radius:14px;overflow:hidden}
.fleet-photo{left:0;top:0;width:412px;height:391px;background:linear-gradient(160deg,#9bb8d8 0%,#6f8f4e 40%,#c99a22 65%,#6b6559 100%)}
.fleet-copy{left:460px;top:48px;width:330px}
.fleet-copy h2{font-size:29px;font-weight:800;color:var(--navy);line-height:1.2}
.fleet-copy h2 span{color:var(--yellow)}
.fleet-copy p{margin-top:22px;font-size:10.5px;line-height:22.5px;color:var(--muted)}
.fleet-copy .btn{position:static;display:inline-flex;margin-top:24px;width:119px;height:33px;background:var(--navy);color:var(--white)}
.slide-arrow{top:1238px;width:58px;height:58px;border-radius:50%;background:var(--yellow);display:flex;align-items:center;justify-content:center}

/* quote banner */
.quote-banner{left:188px;top:1538px;width:824px;height:232px;background:var(--navy);border-radius:14px}
.quote-banner h2{position:absolute;left:50px;top:40px;font-size:29px;font-weight:800;line-height:44px;color:var(--white)}
.quote-banner h2 span{color:var(--yellow)}
.quote-banner .btn{left:50px;top:150px;width:119px;height:33px;border:2px solid var(--yellow);color:var(--yellow)}
.banner-machine{left:702px;top:1520px;width:310px;height:265px;border-radius:10px;background:linear-gradient(150deg,#f3c13a 0%,#d9a21a 45%,#3b3b3b 100%)}

/* about */
.about-heading{left:188px;top:1834px;font-size:30px;font-weight:800;line-height:43px;color:var(--navy)}
.about-heading span{color:var(--yellow)}
.about-copy{left:188px;top:1974px;width:500px;font-size:10.5px;line-height:22.5px;color:var(--ink)}
.about-copy p+p{margin-top:22px}
.about-btn{left:188px;top:2248px;width:119px;height:33px;border:2px solid var(--navy);color:var(--navy)}
.about-photo{left:748px;top:1843px;width:355px;height:441px;border-radius:14px;background:linear-gradient(170deg,#4f86c6 0%,#8aa9c6 35%,#c9782e 60%,#e1ac23 80%,#6d655c 100%)}

/* contact */
.contact-band{left:0;top:2361px;width:1200px;height:802px;background:var(--cream)}
.contact-heading{left:0;top:2420px;width:1200px;text-align:center;font-size:30px;font-weight:800;line-height:44px;color:var(--navy)}
.contact-heading span{color:var(--yellow)}
.contact-photo{left:0;top:2549px;width:688px;height:441px;background:linear-gradient(135deg,#b9b3a8 0%,#8a7a6a 35%,#b4472f 55%,#5a4a3e 100%)}
.contact-form{left:601px;top:2625px;width:449px;height:464px;background:var(--white);border-radius:14px}
.field{position:absolute;left:37px;width:374px;height:38px;border:1px solid #9a9a9a;border-radius:3px;font-size:10px;color:var(--ink);padding:12px 24px}
.field.message{height:125px}
.submit{left:37px;top:380px;width:374px;height:33px;background:var(--navy);color:var(--white)}

/* partners */
.partners{left:0;top:3163px;width:1200px;height:139px;display:flex;align-items:center;justify-content:space-around;padding:0 10px}
.partner-badge{width:140px;height:38px;border-radius:4px;background:#d7dbe4}

/* map */
.map{left:0;top:3302px;width:1200px;height:319px;background:linear-gradient(160deg,#eef0f2 0%,#e6e9ec 50%,#e1e6de 100%)}

/* footer */
.footer-brand{left:188px;top:3690px;font-size:22px}
.footer-contact{left:507px;display:flex;align-items:center;gap:12px;font-size:10.5px;font-weight:600;color:var(--ink)}
.footer-contact .ico{width:17px;height:17px;border-radius:50%;background:var(--yellow);display:flex;align-items:center;justify-content:center}
.social{left:908px;top:3690px;display:flex;gap:12px}
.social i{display:block;width:18px;height:18px;border-radius:50%;background:var(--yellow)}
</style>
</head>
<body>

<header class="abs site-header">
  <div class="abs brand header-brand"><span class="mark"></span>BWH</div>
  <nav class="abs main-nav">
    <span class="active">Home</span><span>About Us</span><span>Plant Hire +</span><span>Major Project Snapshot</span><span>Policies</span><span>Jobs</span>
  </nav>
  <a class="btn header-cta">Contact Us <span class="arrow">›</span></a>
</header>

<section class="abs hero" role="img" aria-label="Yellow wheeled excavator on a dry plain with snow-capped mountains under a blue sky"></section>
<h1 class="abs hero-title">BWH <span>PLANT HERE</span></h1>
<div class="abs hero-dots"><i></i><i></i><i></i><i class="on"></i><i></i><i></i><i></i></div>

<!-- stats -->
<div class="abs stat" style="left:242px">
  <svg width="44" height="42" viewBox="0 0 44 42"><circle cx="22" cy="24" r="10" fill="#f5b400"/><g stroke="#f5b400" stroke-width="3" stroke-linecap="round"><line x1="22" y1="3" x2="22" y2="8"/><line x1="8" y1="10" x2="11" y2="13"/><line x1="36" y1="10" x2="33" y2="13"/><line x1="3" y1="24" x2="7" y2="24"/><line x1="41" y1="24" x2="37" y2="24"/></g></svg>
  <div class="num">20+</div><div class="label">Years of experience</div>
</div>
<div class="divider abs" style="left:339px"></div>
<div class="abs stat" style="left:426px">
  <svg width="44" height="42" viewBox="0 0 44 42"><rect x="8" y="22" width="22" height="12" rx="2" fill="#f5b400"/><path d="M16 22 L16 6 L34 14 L34 24" stroke="#f5b400" stroke-width="3" fill="none"/><rect x="6" y="35" width="30" height="5" rx="2.5" fill="#f5b400"/></svg>
  <div class="num">100+</div><div class="label">Machines in fleet</div>
</div>
<div class="divider abs" style="left:514px"></div>
<div class="abs stat" style="left:611px">
  <svg width="44" height="48" viewBox="0 0 44 48"><path d="M12 46 L12 22 L18 6 Q22 2 24 8 L22 20 L34 20 Q38 21 37 26 L34 46 Z" fill="#f5b400"/></svg>
  <div class="label">One of QLD's largest<br>suppliers</div>
</div>
<div class="divider abs" style="left:709px"></div>
<div class="abs stat" style="left:795px">
  <svg width="44" height="48" viewBox="0 0 44 48"><circle cx="26" cy="16" r="9" fill="none" stroke="#f5b400" stroke-width="5"/><path d="M4 34 L16 30 L30 34 L40 30 L40 36 L26 44 L4 40 Z" fill="#f5b400"/></svg>
  <div class="label">Onsite servicing</div>
</div>
<div class="divider abs" style="left:881px"></div>
<div class="abs stat" style="left:967px">
  <svg width="44" height="48" viewBox="0 0 44 48"><rect x="6" y="4" width="32" height="7" rx="2" fill="#f5b400"/><rect x="18" y="11" width="8" height="22" fill="#f5b400"/><path d="M16 33 L28 33 L22 46 Z" fill="#f5b400"/></svg>
  <div class="label">Custom machine<br>attachments</div>
</div>

<!-- fleet -->
<section class="abs fleet-band"></section>
<div class="abs fleet-tab active" style="left:188px"><svg width="34" height="28" viewBox="0 0 34 28"><rect x="3" y="14" width="18" height="8" rx="1" fill="#f5b400"/><path d="M14 14 L20 3 L30 9 L30 16" stroke="#f5b400" stroke-width="3" fill="none"/><rect x="2" y="23" width="22" height="4" rx="2" fill="#f5b400"/></svg>EXCAVATORS</div>
<div class="abs fleet-tab" style="left:330px"><svg width="34" height="28" viewBox="0 0 34 28"><rect x="8" y="8" width="16" height="10" rx="1" fill="none" stroke="#444" stroke-width="2"/><circle cx="11" cy="22" r="4" fill="none" stroke="#444" stroke-width="2"/><circle cx="24" cy="22" r="4" fill="none" stroke="#444" stroke-width="2"/><path d="M2 12 L2 24" stroke="#444" stroke-width="2"/></svg>DOZERS</div>
<div class="abs fleet-tab" style="left:473px"><svg width="34" height="28" viewBox="0 0 34 28"><path d="M4 8 L22 8 L22 20 L4 20 Z" fill="none" stroke="#444" stroke-width="2"/><path d="M22 12 L29 12 L32 17 L32 20 L22 20" fill="none" stroke="#444" stroke-width="2"/><circle cx="9" cy="23" r="3" fill="#444"/><circle cx="27" cy="23" r="3" fill="#444"/></svg>DUMP TRUCKS</div>
<div class="abs fleet-tab" style="left:617px"><svg width="34" height="28" viewBox="0 0 34 28"><rect x="10" y="3" width="14" height="12" fill="none" stroke="#444" stroke-width="2"/><path d="M3 16 L31 16" stroke="#444" stroke-width="2"/><circle cx="8" cy="22" r="4" fill="none" stroke="#444" stroke-width="2"/><circle cx="26" cy="22" r="4" fill="none" stroke="#444" stroke-width="2"/></svg>GRADERS</div>
<div class="abs fleet-tab" style="left:759px"><svg width="34" height="28" viewBox="0 0 34 28"><rect x="8" y="4" width="12" height="14" fill="none" stroke="#444" stroke-width="2"/><path d="M20 12 L28 12 L30 20" stroke="#444" stroke-width="2" fill="none"/><circle cx="11" cy="22" r="4" fill="none" stroke="#444" stroke-width="2"/><path d="M2 24 L32 24" stroke="#444" stroke-width="2"/></svg>LOADERS</div>
<div class="abs fleet-tab" style="left:902px"><svg width="34" height="28" viewBox="0 0 34 28"><rect x="12" y="4" width="12" height="14" fill="none" stroke="#444" stroke-width="2"/><path d="M12 10 L4 14 L4 20" stroke="#444" stroke-width="2" fill="none"/><circle cx="14" cy="22" r="3" fill="#444"/><circle cx="24" cy="22" r="3" fill="#444"/></svg>BOBCATS</div>

<article class="abs fleet-card">
  <div class="abs fleet-photo" role="img" aria-label="Yellow tracked excavator parked among tall green trees"></div>
  <div class="abs fleet-copy">
    <h2>EXCAVATOR <span>HIRE .</span></h2>
    <p>With one of the largest fleet of excavators for hire in South East Queensland, at BWH Heavy Equipment we are proud of our large range of diggers. All our excavators and diggers for hire are sourced from reputable brands such as Caterman, Komado, Volden, Dorsan, Hikari and more. We also have specialist machines – such as wheeled excavators for hire, long-reach and chameleon clamshell telescopic</p>
    <a class="btn">Contact Us <span class="arrow">›</span></a>
  </div>
</article>
<div class="abs slide-arrow" style="left:143px"><svg width="14" height="18" viewBox="0 0 14 18"><path d="M10 2 L3 9 L10 16" stroke="#1b1b1b" stroke-width="3" fill="none"/></svg></div>
<div class="abs slide-arrow" style="left:1000px"><svg width="14" height="18" viewBox="0 0 14 18"><path d="M4 2 L11 9 L4 16" stroke="#1b1b1b" stroke-width="3" fill="none"/></svg></div>

<!-- quote banner -->
<section class="abs quote-banner">
  <h2>CONTACT US TODAY FOR A<br><span>FREE QUOTE</span></h2>
  <a class="btn">Get a Quote <span class="arrow">›</span></a>
</section>
<div class="abs banner-machine" role="img" aria-label="Yellow tracked excavator with raised boom"></div>

<!-- about -->
<h2 class="abs about-heading">BWH HEAVY EQUIPMENT HIRE<br><span>COMMITTED TO SUPERIOR<br>QUALITY PLANT HIRE SERVICES.</span></h2>
<div class="abs about-copy">
  <p>Brambleworth Heavy Equipment Hire specialise in the hire of heavy earthmoving, mining and construction machines with specialised attachments and tooling. Our array of machines and attachments is second to none, and we have one of the largest hire fleets available in South East Queensland. If its plant hire you require, then Brambleworth Resources, or BWH as the local's call us – should be the first call you make. Wet or dry hire, we provide excellent operators and quality machines across all makes and models to guarantee you maximum up-time.</p>
  <p>With the customer always in mind, the service provided by Brambleworth is guaranteed to be an unparalleled experience – please view our portfolio of equipment and attachments for hire or contact us directly for your needs.</p>
</div>
<a class="btn about-btn">Read More <span class="arrow">›</span></a>
<div class="abs about-photo" role="img" aria-label="Excavator loading soil into an orange tipper truck under a blue sky"></div>

<!-- contact -->
<section class="abs contact-band"></section>
<h2 class="abs contact-heading">CONTACT US TODAY FOR A<br><span>FREE QUOTE</span></h2>
<div class="abs contact-photo" role="img" aria-label="Red demolition crane among apartment buildings and rubble"></div>
<form class="abs contact-form">
  <div class="field" style="top:50px">Full Name</div>
  <div class="field" style="top:110px">Email Address</div>
  <div class="field" style="top:170px">Phone No</div>
  <div class="field message" style="top:232px">Enquiry</div>
  <a class="btn submit">Submit <span class="arrow">›</span></a>
</form>

<!-- partners -->
<section class="abs partners">
  <span class="partner-badge"></span><span class="partner-badge"></span><span class="partner-badge"></span><span class="partner-badge"></span><span class="partner-badge"></span><span class="partner-badge"></span>
</section>

<div class="abs map" role="img" aria-label="Street map of the depot location with a red location pin"></div>

<!-- footer -->
<footer>
  <div class="abs brand footer-brand"><span class="mark"></span>BWH</div>
  <div class="abs footer-contact" style="top:3677px"><span class="ico"><svg width="9" height="9" viewBox="0 0 10 10"><path d="M2 1 L4 1 L5 3 L4 4 Q5 6 6 6 L7 5 L9 6 L9 8 Q8 9 7 9 Q1 8 1 2 Q1 1 2 1Z" fill="#1b1b1b"/></svg></span>1300 555 014</div>
  <div class="abs footer-contact" style="top:3714px"><span class="ico"><svg width="9" height="10" viewBox="0 0 10 12"><path d="M5 11 Q1 6 1 4 A4 4 0 0 1 9 4 Q9 6 5 11Z" fill="#1b1b1b"/><circle cx="5" cy="4" r="1.5" fill="#f5b400"/></svg></span>18 Saltbush Rd, Kelvale QLD 4210</div>
  <div class="abs social"><i></i><i></i><i></i><i></i></div>
</footer>

</body>
</html>
```